Stationery Design for QORV

I have now selected the logo for my consultancy company. I need some innovative design for my stationary. The audience is senior executives in international banks predominantly in Asia, but also in the Middle East, Africa and Latin America.
My company advises them on solutions to be able to grow their business.

I will update to a vector file in a few hours

Target Market(s)

Senior executives in international Banks.

Industry/Entity Type

Business

Requirements
Should not have
• It should not be forgettable!

```html
<!DOCTYPE html>
<html lang="en">
<head>
<meta charset="utf-8">
<title>QORV Stationery</title>
<link rel="stylesheet" href="https://fonts.googleapis.com/css2?family=Open+Sans:wght@300;400&display=swap">
<style>
  :root {
    --bg: #e9e7e4;
    --paper: #ffffff;
    --charcoal: #55595d;
    --charcoal-dark: #404347;
    --charcoal-light: #6a6e72;
    --lime: #b6d233;
    --ink: #4a4d50;
    --ink-soft: #8a8d90;
    --rule: #d6d6d6;
  }
  * { box-sizing: border-box; margin: 0; padding: 0; }
  html, body { width: 1200px; height: 1160px; overflow: hidden; }
  body {
    background: var(--bg);
    font-family: "Open Sans", Arial, sans-serif;
    color: var(--ink);
    position: relative;
  }
  .sheet { position: absolute; box-shadow: 0 4px 14px rgba(0,0,0,.18); }

  .brand { display: flex; align-items: center; gap: 12px; }
  .brand-dot { border-radius: 50%; background: var(--lime); flex: none; }
  .brand-name { font-weight: 300; letter-spacing: .08em; }

  /* Presentation folder */
  .folder {
    left: 60px; top: 70px; width: 480px; height: 650px;
    background: linear-gradient(115deg, var(--charcoal-dark) 0%, var(--charcoal-light) 45%, var(--charcoal-dark) 100%);
    display: flex; align-items: center; justify-content: center;
  }
  .folder .brand { flex-direction: column; gap: 14px; }
  .folder .brand-dot { width: 76px; height: 76px; }
  .folder .brand-name { color: var(--paper); font-size: 34px; }

  /* Letterhead */
  .letterhead {
    left: 580px; top: 60px; width: 560px; height: 770px;
    background: var(--paper); padding: 40px 44px;
  }
  .letterhead-header { display: flex; justify-content: space-between; align-items: flex-start; }
  .letterhead .brand-dot { width: 40px; height: 40px; }
  .letterhead .brand-name { font-size: 22px; color: var(--ink); }
  .letterhead-contact { font-size: 7.5px; line-height: 1.6; text-align: right; color: var(--ink); font-style: normal; }
  .letter-body { margin-top: 64px; font-size: 9.5px; line-height: 1.55; text-align: justify; }
  .letter-body p { margin-bottom: 14px; }
  .letterhead-mark {
    position: absolute; right: 50px; bottom: 40px; width: 130px; height: 130px;
    border-radius: 50%; background: var(--lime); opacity: .14;
  }

  /* Envelope */
  .envelope {
    left: 60px; top: 790px; width: 640px; height: 300px;
    background: var(--paper); display: flex;
  }
  .envelope-band { width: 24px; background: var(--charcoal); }
  .envelope-accent { width: 6px; background: var(--lime); }
  .envelope-content { padding: 26px 24px; }
  .envelope .brand-dot { width: 38px; height: 38px; }
  .envelope .brand-name { font-size: 22px; color: var(--ink); }
  .envelope-address { font-size: 9px; margin: 6px 0 0 50px; color: var(--ink); }

  /* Business cards */
  .card { width: 220px; height: 132px; }
  .card-back {
    left: 730px; top: 870px; background: var(--charcoal);
    display: flex; align-items: center; justify-content: center;
  }
  .card-back .brand-dot { width: 40px; height: 40px; }
  .card-back-url { position: absolute; right: 10px; bottom: 8px; font-size: 6px; color: var(--paper); }
  .card-front {
    left: 965px; top: 870px; background: var(--paper);
    display: flex; align-items: center; padding: 0 14px;
  }
  .card-front .brand { flex-direction: column; gap: 6px; width: 70px; }
  .card-front .brand-dot { width: 22px; height: 22px; }
  .card-front .brand-name { font-size: 12px; color: var(--ink); }
  .card-divider { width: 1px; height: 84px; background: var(--rule); margin: 0 14px; }
  .card-person { font-size: 10px; margin-bottom: 10px; }
  .card-details { font-size: 5.5px; line-height: 1.7; color: var(--ink-soft); }
</style>
</head>
<body>

  <section class="sheet folder">
    <div class="brand">
      <span class="brand-dot"></span>
      <span class="brand-name">QORV</span>
    </div>
  </section>

  <section class="sheet letterhead">
    <header class="letterhead-header">
      <div class="brand">
        <span class="brand-dot"></span>
        <span class="brand-name">QORV</span>
      </div>
      <address class="letterhead-contact">
        88 Harbour Road, Kowloon 10000, Hong Kong<br>
        Phone: +852 2917 4460<br>
        Fax: +852 2917 4461<br>
        www.qorv.com
      </address>
    </header>
    <div class="letter-body">
      <p>Lorem ipsum dolor sit amet, consectetur adipiscing elit. Nunc imperdiet ultricies viverra. Vestibulum mattis imperdiet lacus, non dignissim nulla facilisis vitae.</p>
      <p>Integer libero diam, interdum in condimentum dignissim, lacinia eu libero. Vivamus sodales dignissim sodales. Nulla felis nunc, posuere ut mollis eget, viverra vitae quam.</p>
      <p>Donec laoreet mi sed dolor lacinia varius. Aenean a nisl nec mi imperdiet interdum at consequat massa.</p>
      <p>Sed dolor ipsum, pharetra dignissim elit. Integer elit ligula, tristique non lacinia et, ornare in nisl.</p>
      <p>Nam tempus est id consectetur. Suspendisse consectetur tempor tincidunt. Integer tincidunt tortor mi at tristique. Vivamus egestas varius elementum. Donec convallis ultricies felis. Aliquam tristique tincidunt massa, in ullamcorper arcu imperdiet nec.</p>
      <p>Aenean leo rhoncus vulputate. Fusce ut velit massa, ac fringilla nibh. Cras quis lacus eget cursus nibh. Etiam bibendum diam id sapien lobortis iaculis.</p>
      <p>Sed ligula laoreet hendrerit. Aliquam erat volutpat. Sed porttitor iaculis lorem sodales aliquet. Morbi rhoncus imperdiet pellentesque.</p>
      <p>Vivamus diam. Morbi aliquet risus eget orci fermentum adipiscing. Donec tempor iaculis congue felis hendrerit.</p>
    </div>
    <span class="letterhead-mark" aria-hidden="true"></span>
  </section>

  <section class="sheet envelope">
    <div class="envelope-band"></div>
    <div class="envelope-accent"></div>
    <div class="envelope-content">
      <div class="brand">
        <span class="brand-dot"></span>
        <span class="brand-name">QORV</span>
      </div>
      <p class="envelope-address">88 Harbour Road, Kowloon 10000, Hong Kong</p>
    </div>
  </section>

  <section class="sheet card card-back">
    <span class="brand-dot"></span>
    <span class="card-back-url">www.qorv.com</span>
  </section>

  <section class="sheet card card-front">
    <div class="brand">
      <span class="brand-dot"></span>
      <span class="brand-name">QORV</span>
    </div>
    <span class="card-divider"></span>
    <div>
      <p class="card-person">Lena Marsh</p>
      <p class="card-details">
        +852 2917 4460<br>
        88 Harbour Road, Kowloon<br>
        Hong Kong<br>
        hello@qorv.com<br>
        www.qorv.com
      </p>
    </div>
  </section>

</body>
</html>
```